Business Cards Needed For Veterinary Business

Looking for a business card design for a veterinary blood bank. We would like it to be clean and professional on appearance but still warm and inviting. We would like to utilize our logo and similar coloring. We will use our phone number, email, website, employee name, employee title.

We do not want a bunch of animated animal photos but do not need the style to be as clinical as a laboratory or human medical procedure office.

We are looking for some creative ideas to choose from so that we can generate a standout professional business card for our management team to utilize.

Target Market(s)

professionals

Industry/Entity Type

veterinary

Contact Information for Business Card

employee name, employee title, phone number, website URL, email

Font styles to use
Sans Serif

Colors
0054AA
0677BA
7BADD7
CADEEF
E8F1F8
EB3D1F
EC4F4E
F09395
F8D3D4
FCEDEE

Requirements
Nice to have
• creative design
Should not have
• animated photos

```html
<!DOCTYPE html>
<html lang="en">
<head>
<meta charset="UTF-8">
<title>Veterinarian Business Card</title>
<link href="https://fonts.googleapis.com/css2?family=Roboto:wght@300;400;500&display=swap" rel="stylesheet">
<style>
  :root {
    --red: #e4161f;
    --red-deep: #d91e2c;
    --track: #f2f2f2;
    --ink: #222222;
    --ink-soft: #333333;
    --paper: #ffffff;
  }
  * { margin: 0; padding: 0; box-sizing: border-box; }
  html, body { width: 1200px; height: 763px; overflow: hidden; background: var(--paper); }
  .card {
    position: relative;
    width: 1200px;
    height: 763px;
    background: var(--paper);
    font-family: "Roboto", Arial, sans-serif;
    overflow: hidden;
  }
  .edge-bar {
    position: absolute; left: 0; top: 151px;
    width: 12px; height: 450px;
    background: var(--red-deep);
    border-radius: 0 3px 3px 0;
  }
  .icon-track {
    position: absolute; left: 148px; top: 156px;
    width: 54px; height: 438px;
    background: var(--track);
    border-radius: 8px;
  }
  .icon {
    position: absolute; left: 148px;
    width: 54px; height: 58px;
    background: var(--red);
    border-radius: 8px;
    display: flex; align-items: center; justify-content: center;
  }
  .icon--person { top: 162px; background: transparent; }
  .icon--phone { top: 354px; }
  .icon--mail { top: 445px; }
  .icon--pin { top: 538px; }
  .name {
    position: absolute; left: 242px; top: 146px;
    font-size: 49px; font-weight: 500; color: var(--ink);
    letter-spacing: 0.2px;
  }
  .title {
    position: absolute; left: 252px; top: 205px;
    font-size: 28px; font-weight: 300; color: var(--ink-soft);
  }
  .contact {
    position: absolute; left: 246px;
    font-size: 28px; font-weight: 300; color: var(--ink-soft);
    line-height: 39px;
  }
  .contact--phone { top: 343px; }
  .contact--web { top: 436px; }
  .contact--address { top: 528px; }
  .feature {
    position: absolute; right: 0; top: 0;
    width: 580px; height: 763px;
  }
</style>
</head>
<body>
<div class="card">
  <div class="edge-bar"></div>
  <div class="icon-track"></div>

  <div class="icon icon--person">
    <svg width="44" height="70" viewBox="0 0 44 70">
      <circle cx="22" cy="17" r="15" fill="var(--red)"/>
      <path d="M0 50 Q0 36 14 36 H30 Q44 36 44 50 V62 Q44 70 36 70 H8 Q0 70 0 62 Z" fill="var(--red)"/>
    </svg>
  </div>
  <div class="icon icon--phone">
    <svg width="30" height="30" viewBox="0 0 24 24">
      <path fill="#fff" d="M6.6 10.8a15.1 15.1 0 0 0 6.6 6.6l2.2-2.2a1 1 0 0 1 1-.25 11.4 11.4 0 0 0 3.6.57 1 1 0 0 1 1 1V20a1 1 0 0 1-1 1A17 17 0 0 1 3 4a1 1 0 0 1 1-1h3.5a1 1 0 0 1 1 1c0 1.25.2 2.45.57 3.57a1 1 0 0 1-.25 1z"/>
    </svg>
  </div>
  <div class="icon icon--mail">
    <svg width="30" height="22" viewBox="0 0 30 22">
      <rect x="1" y="1" width="28" height="20" fill="none" stroke="#fff" stroke-width="2"/>
      <path d="M1 1 L15 13 L29 1 M1 21 L11 10 M29 21 L19 10" fill="none" stroke="#fff" stroke-width="2"/>
    </svg>
  </div>
  <div class="icon icon--pin">
    <svg width="22" height="30" viewBox="0 0 22 30">
      <path fill="#fff" d="M11 0C5 0 0 4.7 0 10.6 0 18 11 30 11 30s11-12 11-19.4C22 4.7 17 0 11 0zm0 15a4.5 4.5 0 1 1 0-9 4.5 4.5 0 0 1 0 9z"/>
    </svg>
  </div>

  <h1 class="name">Daniel Harper</h1>
  <p class="title">Veterinarian</p>

  <div class="contact contact--phone">
    <div>+000 123 456 7890</div>
    <div>+000 123 456 7890</div>
  </div>
  <div class="contact contact--web">
    <div>yourmail@name.com</div>
    <div>www.websitename.com</div>
  </div>
  <div class="contact contact--address">
    <div>your street nmae here</div>
    <div>New Yerk City, Zip - 000</div>
  </div>

  <svg class="feature" viewBox="620 0 580 763" role="img" aria-label="Photo of a ginger cat wearing round sunglasses on torn red paper">
    <defs>
      <linearGradient id="featureTone" x1="0" y1="0" x2="1" y2="0.3">
        <stop offset="0" stop-color="#d81b2c"/>
        <stop offset="0.35" stop-color="#e0302c"/>
        <stop offset="0.7" stop-color="#e66a3a"/>
        <stop offset="1" stop-color="#efa074"/>
      </linearGradient>
    </defs>
    <path fill="url(#featureTone)" d="M714 0 L1200 0 L1200 763 L628 763 L634 735 L640 700 L646 660 L650 620 L656 580 L652 540 L660 500 L664 462 L668 430 L666 400 L672 360 L676 320 L682 280 L686 240 L692 200 L696 165 L700 130 L704 95 L708 60 L711 30 Z"/>
  </svg>
</div>
</body>
</html>
```